Natural Health Supplement Company Needs a Product Label Designed

HARVEST ROOT LABS needs a PROBIOTICS product label designed.We are a natural health vitamin and dietary supplement company. Who ever wins will have the opportunity to design a lot more product labels for us.
Product name: PROBIOTICS
*Please use the attached logo and base the label text exactly off the Kelt Wellness label example.
Other product examples have been attached for inspiration.

Colors

Designer to choose colors to be used in the design.

Requirements
Must have
• Product name: PROBIOTICS
• *Please use the attached logo and base the label text exactly off the Kelt Wellness label example.
• Other product examples have been attached for inspiration.

```html
<!DOCTYPE html>
<html lang="en">
<head>
<meta charset="utf-8">
<title>Harvest Root Labs – Probiotics-40 Label</title>
<link href="https://fonts.googleapis.com/css2?family=Libre+Baskerville:wght@400;700&family=Montserrat:wght@400;500;600;700&family=Arimo:wght@400;700&display=swap" rel="stylesheet">
<style>
  :root {
    --green: #7dc242;
    --green-dark: #5ea52c;
    --green-light: #c4e7a0;
    --grey: #6b6e70;
    --ink: #222;
    --paper: #ffffff;
    --bg: #f4f5f3;
  }
  * { margin: 0; padding: 0; box-sizing: border-box; }
  html, body { width: 1200px; height: 1200px; overflow: hidden; background: var(--bg); }
  .canvas { position: relative; width: 1200px; height: 1200px; }

  .label {
    position: absolute; left: 30px; top: 300px; width: 1140px; height: 600px;
    background: var(--paper); box-shadow: 0 6px 30px rgba(0,0,0,.12);
    display: flex; overflow: hidden;
  }
  .label__stripe {
    position: absolute; left: 0; right: 0; bottom: 34px; height: 10px; background: var(--green);
  }
  .panel { position: relative; height: 100%; }
  .panel--info { width: 340px; padding: 70px 26px 0 30px; font-family: "Montserrat", sans-serif; color: var(--ink); }
  .panel--front { width: 440px; text-align: center; border-left: 1px dashed #e3e3e3; border-right: 1px dashed #e3e3e3; }
  .panel--facts { width: 360px; padding: 52px 24px 0 20px; font-family: "Arimo", sans-serif; color: var(--ink); }

  .info__text { font-size: 11.5px; line-height: 1.45; margin-bottom: 16px; }
  .info__box { border: 1px solid #333; padding: 12px 14px; font-size: 12px; line-height: 1.4; margin-bottom: 20px; }

  .brand { margin-top: 58px; }
  .brand__name {
    font-family: "Libre Baskerville", serif; font-weight: 700; font-size: 30px;
    color: var(--green); letter-spacing: 1px;
  }
  .brand__dot { display: inline-block; width: 12px; height: 12px; border-radius: 50%; background: var(--green); margin-right: 8px; vertical-align: middle; }
  .product { margin-top: 26px; font-family: "Libre Baskerville", serif; font-weight: 700; text-align: left; padding-left: 52px; }
  .product__pro { font-size: 40px; color: var(--green); line-height: 1; }
  .product__name { font-size: 56px; color: var(--grey); line-height: 1.05; }
  .product__name span { color: var(--green); }
  .product__count { font-family: "Montserrat", sans-serif; font-weight: 500; font-size: 30px; color: #4a4c4e; text-align: center; letter-spacing: 1px; margin-top: 6px; }

  .capsules {
    position: absolute; left: 22px; top: 380px; width: 300px; height: 120px;
    background: radial-gradient(ellipse at center, #7fd35a 0%, #b9e69a 55%, rgba(255,255,255,0) 72%);
  }
  .badge {
    position: absolute; right: 26px; top: 370px; width: 132px; height: 132px;
    border: 3px solid var(--green-dark); border-radius: 50%;
    display: flex; align-items: center; justify-content: center;
    font-family: "Montserrat", sans-serif; font-weight: 600; font-size: 17px; line-height: 1.2; color: #333;
  }
  .tagline {
    position: absolute; left: 0; right: 0; bottom: 58px;
    font-family: "Montserrat", sans-serif; font-weight: 700; font-size: 34px; letter-spacing: 2px;
  }
  .tagline__a { color: var(--green); }
  .tagline__b { color: #555; }

  .facts { border: 1px solid #333; padding: 6px 8px; }
  .facts__title { font-weight: 700; font-size: 24px; }
  .facts__meta { font-size: 14px; line-height: 1.3; border-bottom: 6px solid #222; padding-bottom: 8px; }
  .facts__head { display: flex; justify-content: flex-end; gap: 12px; font-size: 10px; text-align: right; padding: 4px 0; border-bottom: 3px solid #222; }
  .facts__row { display: flex; font-size: 12.5px; border-bottom: 1px solid #333; padding: 1px 0; }
  .facts__row span:first-child { flex: 1; }
  .facts__row span:nth-child(2) { width: 80px; }
  .facts__row span:last-child { width: 14px; text-align: right; }
  .facts__row--gap { border-bottom-width: 3px; }
  .facts__note { font-size: 9.5px; line-height: 1.1; padding: 3px 0; border-bottom: 6px solid #222; }
  .facts__foot { font-size: 11px; padding-top: 3px; }
  .directions { font-size: 12.5px; line-height: 1.3; margin-top: 12px; }
  .directions p { margin-bottom: 4px; }
  .disclaimer { border: 1px solid #333; font-weight: 700; font-size: 11px; line-height: 1.25; padding: 4px 6px; margin-top: 6px; }
</style>
</head>
<body>
<div class="canvas">
  <div class="label">
    <section class="panel panel--info">
      <p class="info__text">Lorem Ipsum is simply dummy text of the printing and typesetting industry. Lorem Ipsum has been the industry's standard dummy text ever since the 1500s, when an unknown printer took a galley of type and scrambled it to make a type specimen book.</p>
      <p class="info__text">It has survived not only five centuries, but also the leap into electronic typesetting, remaining essentially unchanged. It was popularised in the 1960s with the release of Linotext sheets containing Lorem Ipsum passages, and more recently with desktop publishing software like Folio Layout including versions of Lorem Ipsum.</p>
      <div class="info__box">Contrary to popular belief, Lorem Ipsum is not simply random text. It has roots in a piece of classical Latin literature from 45 BC, making it over 2000 years old.</div>
      <p class="info__text">It is a long established fact that a reader will be distracted by the readable content of a page when looking at its layout.</p>
    </section>

    <section class="panel panel--front">
      <div class="brand"><span class="brand__dot"></span><span class="brand__name">HARVEST ROOT LABS</span></div>
      <div class="product">
        <div class="product__pro">PRO</div>
        <div class="product__name">BIOTICS-<span>40</span></div>
      </div>
      <div class="product__count">40 BILLION</div>
      <div class="capsules" role="img" aria-label="Pile of green two-tone probiotic capsules"></div>
      <div class="badge">ANY<br>CAPSULS<br>COUNT</div>
      <div class="tagline"><span class="tagline__a">PRIVATE</span> <span class="tagline__b">LABELING</span></div>
    </section>

    <section class="panel panel--facts">
      <div class="facts">
        <div class="facts__title">Supplement Facts</div>
        <div class="facts__meta">Serving Size - 1 Capsule<br>Servings Per Container - 90</div>
        <div class="facts__head"><span>Amount per<br>Serving</span><span>% Daily Value</span></div>
        <div class="facts__row"><span>L. acidophilus (LA-14)</span><span>5 billion</span><span>†</span></div>
        <div class="facts__row"><span>L. rhamnosus</span><span>5 billion</span><span>†</span></div>
        <div class="facts__row facts__row--gap"><span>L. plantarum</span><span>5 billion</span><span>†</span></div>
        <div class="facts__row"><span>B. longum</span><span>5 billion</span><span>†</span></div>
        <div class="facts__row"><span>B. bifidum</span><span>5 billion</span><span>†</span></div>
        <div class="facts__note">Proprietary blend containing over 25 billion live, active bacteria at the time of manufacture.</div>
        <div class="facts__foot">† Daily Value not established.</div>
      </div>
      <div class="directions">
        <p><b>Other Ingredients:</b> Rice Flour (as bulk), Vegetable Capsules as acid resistant AcidGuard caps™, Organic Pure-Mag™ (as anti-caking agent).</p>
        <p><b>Suggested Use:</b> Take 1 capsule daily, preferably in the morning on an empty stomach (at least 30 minutes before meal). Or use as directed by your healthcare professional.</p>
      </div>
      <div class="disclaimer">*These statements have not been evaluated by the Food and Drug Administration. This product is not intended to diagnose, treat, cure, or prevent any disease.</div>
    </section>

    <div class="label__stripe"></div>
  </div>
</div>
</body>
</html>
```